Logistics Website Design

See website https://tvarfreightglobal.com for theme and color details. Need the site to be re-done and reflect some of the designs shown in this list here: https://pinvora.com/tags/logistics-company-website

Target Market(s)

Logistics & Transportation

Industry/Entity Type

Logistics and Supply Chain

Coding

Coded - Design and coding required

Number of Pages Required

5+ page

Requirements
Must have
• Colors must match theme of logo. Looking for a sleek, interactive design.

```html
<!DOCTYPE html>
<html lang="en">
<head>
<meta charset="UTF-8">
<title>Tvar Freight — Logistics</title>
<link rel="stylesheet" href="https://fonts.googleapis.com/css2?family=Montserrat:wght@500;600;700;800&family=Open+Sans:ital,wght@0,400;0,600;1,400&display=swap">
<style>
:root{
  --orange:#e8641b;
  --ink:#141414;
  --text:#333;
  --muted:#666;
  --white:#fff;
  --footer:#1c1410;
  --footer-text:#d9d2cc;
}
*{margin:0;padding:0;box-sizing:border-box}
html,body{width:748px;height:1200px;overflow:hidden;background:var(--white)}
body{font-family:"Open Sans",Arial,sans-serif;color:var(--text);position:relative}
.nav{height:35px;display:flex;justify-content:flex-end;align-items:center;padding-right:150px;gap:22px;font-family:"Montserrat",sans-serif;font-size:8.5px;font-weight:500;color:var(--ink);background:var(--white)}
.nav .active{border-bottom:1.5px solid var(--orange);padding-bottom:2px}
.hero{position:absolute;top:35px;left:0;width:748px;height:322px;background:linear-gradient(100deg,#1a0f0a 0%,#3a1a0e 30%,#8a3512 60%,#d96a25 82%,#f09a45 100%)}
.hero-photo{position:absolute;right:40px;top:40px;width:300px;height:250px;border-radius:6px;background:linear-gradient(160deg,#7a1a14 0%,#b0241a 45%,#3a1410 100%);opacity:.85}
.road{position:absolute;left:0;bottom:0;width:100%;height:70px;background:linear-gradient(180deg,rgba(30,20,15,0) 0%,#1d1612 100%)}
.brand{position:absolute;display:flex;align-items:center;gap:8px;font-family:"Montserrat",sans-serif;font-weight:800;font-size:15px;color:var(--white);letter-spacing:.5px}
.brand .dot{width:34px;height:34px;border-radius:50%;background:var(--orange)}
.hero .brand{left:70px;top:32px}
.hero h1{position:absolute;left:70px;top:195px;font-family:"Montserrat",sans-serif;font-weight:800;font-size:21px;line-height:25px;color:var(--white);letter-spacing:.3px}
.hero p{position:absolute;left:70px;top:250px;width:210px;font-size:10.5px;line-height:13px;color:var(--white)}
.btn{position:absolute;left:70px;top:280px;background:var(--orange);color:var(--white);font-size:8px;font-weight:600;padding:6px 12px;border-radius:2px}
.intro{position:absolute;top:362px;left:0;width:748px;text-align:center}
.intro h2{font-family:"Montserrat",sans-serif;font-weight:600;font-size:25px;color:var(--ink)}
.intro p{width:520px;margin:8px auto 0;font-style:italic;font-size:10px;line-height:14px;color:var(--muted)}
.services-title{position:absolute;top:486px;width:748px;text-align:center;font-family:"Montserrat",sans-serif;font-weight:600;font-size:28px;color:var(--ink)}
.grid{position:absolute;top:533px;left:112px;display:grid;grid-template-columns:252px 252px;column-gap:16px;row-gap:14px}
.card{text-align:center}
.card .photo{height:142px}
.card h3{font-family:"Montserrat",sans-serif;font-weight:700;font-size:14px;line-height:16px;color:var(--ink);margin-top:6px}
.card p{font-size:7.5px;line-height:10px;color:var(--muted);width:200px;margin:5px auto 0}
.footer{position:absolute;top:995px;left:0;width:748px;height:205px;background:var(--footer);color:var(--footer-text)}
.footer .brand{left:112px;top:38px}
.footer .about{position:absolute;left:112px;top:130px;width:270px;font-size:7.5px;line-height:10px}
.footer .contact{position:absolute;left:112px;top:162px;font-size:7.5px;color:var(--white)}
.footer .links{position:absolute;left:468px;top:22px;list-style:none;font-size:8px;line-height:13px;color:var(--white)}
.footer .links li:first-child{font-weight:600;margin-bottom:4px}
</style>
</head>
<body>
<nav class="nav">
  <span class="active">Home</span><span>Services ▾</span><span>Industries ▾</span><span>Request a Quote</span><span>About Us</span><span>Contact Us</span>
</nav>

<section class="hero">
  <div class="hero-photo" role="img" aria-label="Red semi truck driving on a highway at sunset"></div>
  <div class="road"></div>
  <div class="brand"><span class="dot"></span>Tvar Freight</div>
  <h1>DELIVERING STRENGTH<br>IN EVERY MILE</h1>
  <p>Secure and reliable transportation for all your cargo needs.</p>
  <span class="btn">Request a Quote</span>
</section>

<section class="intro">
  <h2>Keeping Your Supply Chain Moving</h2>
  <p>We deliver a comprehensive range of open deck and specialized transportation services including flatbed, step deck, heavy haul, and over-dimensional freight solutions. Backed by years of experience, a trusted nationwide carrier network, and a strong safety-first culture, we provide reliable, adaptable logistics support built around the unique requirements of every load.</p>
</section>

<h2 class="services-title">Our Services</h2>
<div class="grid">
  <div class="card">
    <div class="photo" role="img" aria-label="Blue truck hauling lumber on a flatbed trailer" style="background:linear-gradient(180deg,#9cc4ea 0%,#c9dcec 55%,#5b6b7c 100%)"></div>
    <h3>Flatbed<br>Transportation</h3>
    <p>From lumber and steel to machinery, our flatbed fleet handles open loads with care and secure tie-downs.</p>
  </div>
  <div class="card">
    <div class="photo" role="img" aria-label="Truck pulling a step deck trailer with machinery" style="background:linear-gradient(180deg,#c8d6e2 0%,#e4e9ee 50%,#4a5867 100%)"></div>
    <h3>Step Deck<br>Transportation</h3>
    <p>Our step deck trailers carry taller cargo with lower deck heights for easy loading and legal clearance.</p>
  </div>
  <div class="card">
    <div class="photo" role="img" aria-label="White dry van trailer on a road" style="background:linear-gradient(180deg,#d6dde4 0%,#f1f3f5 50%,#7c8590 100%)"></div>
    <h3>Dry Van<br>Transportation</h3>
    <p>From consumer goods to industrial materials, our dry vans keep freight safe, dry and on schedule.</p>
  </div>
  <div class="card">
    <div class="photo" role="img" aria-label="Heavy haul trucks lined up at dusk" style="background:linear-gradient(180deg,#6f86a8 0%,#b9a69a 50%,#2c2a33 100%)"></div>
    <h3>Heavy Haul<br>Transportation</h3>
    <p>We provide heavy haul solutions for oversized, overweight and over-dimensional freight.</p>
  </div>
</div>

<footer class="footer">
  <div class="brand"><span class="dot"></span>Tvar Freight</div>
  <p class="about">Lorem ipsum dolor sit amet, consectetur adipiscing elit, sed do eiusmod tempor incididunt ut labore et dolore magna aliqua.</p>
  <p class="contact">Call 24/7: +1 (123) 456-7890 &nbsp;&nbsp; Email: info@example.com</p>
  <ul class="links">
    <li>Our Navigation</li><li>Home</li><li>Industries</li><li>Request a Quote</li><li>About Us</li><li>Contact Us</li>
  </ul>
</footer>
</body>
</html>
```